Football and sports news website

I am looking for a good design and website for a Sports news and Football website. The website will carry mainly football news from different leagues across Europe and the rest of the World. There will be a category for football, tennis, basketball, cricket,ruby. My website should be contemporary and attractive. My favorite colors are blue, purple,orange and red.
Designers can take a clue from http://kelvarodaily.com
There will be column at the under of every news page in which readers of the article can comment.

Industry/Entity Type

News

Coding

Coded - Design and coding required

```html
<!DOCTYPE html>
<html lang="en">
<head>
<meta charset="utf-8">
<title>Harlow Sports</title>
<link href="https://fonts.googleapis.com/css2?family=Open+Sans:wght@400;600;700&family=Roboto+Condensed:wght@400;700&display=swap" rel="stylesheet">
<style>
:root{
  --blue:#2d8ed3;
  --red:#e3202c;
  --dark:#1c1c1c;
  --darker:#141414;
  --ink:#333;
  --muted:#777;
  --line:#e6e6e6;
  --white:#fff;
  --star:#f0a020;
}
*{margin:0;padding:0;box-sizing:border-box}
html,body{width:1200px;height:3237px;overflow:hidden}
body{position:relative;background:var(--white);font-family:"Open Sans",sans-serif;color:var(--ink)}
.abs{position:absolute}
/* top bar */
.top-bar{left:0;top:0;width:1200px;height:34px;background:var(--dark);color:#ddd;font-size:13px}
.top-links{left:97px;top:0;display:flex;height:34px;align-items:center}
.top-links span{padding:0 20px;border-right:1px solid #333;line-height:34px}
.top-links span:first-child{padding-left:0}
.top-call{left:680px;top:0;height:34px;display:flex;align-items:center;gap:10px}
.top-social{left:920px;top:11px;display:flex;gap:8px}
.top-social i{width:12px;height:12px;background:#ccc;display:block}
.top-search{left:1045px;top:0;width:55px;height:34px;background:var(--white);display:flex;align-items:center;justify-content:center}
/* header */
.site-header{left:0;top:34px;width:1200px;height:84px;border-bottom:1px solid var(--line)}
.brand{left:97px;top:22px;font-family:"Roboto Condensed",sans-serif;font-weight:700;font-size:34px;letter-spacing:1px;color:var(--darker);display:flex;align-items:center;gap:8px}
.brand-dot{width:22px;height:22px;border-radius:50%;background:var(--red)}
.main-nav{left:458px;top:32px;display:flex;font-family:"Roboto Condensed",sans-serif;font-size:13.5px;color:var(--darker);text-transform:uppercase}
.main-nav span{margin-right:44px}
.main-nav span:last-child{margin-right:0}
/* hero */
.hero{left:0;top:118px;width:1200px;height:465px;background:radial-gradient(ellipse at 25% 20%,#7f93a8 0%,#2c3d52 35%,#0d1622 75%)}
.hero-figure{left:480px;top:0;width:620px;height:465px;background:radial-gradient(ellipse at 55% 45%,rgba(200,60,60,.55) 0%,rgba(60,80,130,.35) 40%,transparent 70%)}
.hero-caption{left:97px;top:331px;width:1003px;height:134px;background:rgba(20,20,20,.72);color:var(--white);padding:24px 40px 0 40px}
.hero-caption h1{font-family:"Roboto Condensed",sans-serif;font-weight:700;font-size:30px;letter-spacing:.5px}
.hero-caption p{font-size:13px;line-height:22px;width:860px;margin-top:6px}
.hero-arrows{right:30px;top:52px}
/* section titles */
.section-title{font-family:"Roboto Condensed",sans-serif;font-weight:400;font-size:26px;color:var(--darker);text-transform:uppercase}
.section-title.blue{color:var(--blue);font-size:24px}
/* post card */
.post-card{left:97px;width:697px;border:1px solid var(--line);padding:17px}
.post-image{position:relative;width:661px;height:242px}
.tag-big{position:absolute;left:0;bottom:0;background:var(--red);color:var(--white);font-family:"Roboto Condensed",sans-serif;font-size:17px;padding:8px 12px}
.post-head{display:flex;gap:14px;margin-top:16px}
.post-icon{width:38px;height:38px;border-radius:50%;border:2px solid #f3c6c9;display:flex;align-items:center;justify-content:center;flex:none}
.post-title{font-size:17px;color:#444;line-height:22px}
.post-meta{display:flex;gap:26px;font-size:10.5px;color:var(--muted);font-style:italic;margin-top:6px}
.excerpt{font-size:11.5px;line-height:21px;color:#555;margin-top:14px}
.more{font-size:11px;color:#444;margin-top:14px;text-transform:uppercase}
/* news grid */
.news-item{width:330px}
.news-image{width:330px;height:162px}
.news-head{display:flex;align-items:center;gap:12px;margin-top:22px}
.tag-small{background:var(--red);color:var(--white);font-size:11px;padding:2px 8px}
.news-title{font-size:16.5px;color:#333}
.news-item .excerpt{margin-top:10px;font-size:11.5px;line-height:20px}
.news-foot{display:flex;align-items:center;gap:22px;margin-top:14px;font-size:11.5px;color:#666}
.stars{color:var(--star);letter-spacing:1px;font-size:11px}
.stars b{color:#ccc;font-weight:400}
/* sidebar */
.side-head{left:829px;width:271px;height:43px;background:var(--blue);color:var(--white);font-family:"Roboto Condensed",sans-serif;font-size:17px;padding:11px 16px;text-transform:uppercase}
.fixture-title{left:829px;width:271px;text-align:center;font-size:12.5px;line-height:17px;color:#222}
.fixture-title b{font-weight:600;display:block;text-transform:uppercase}
.score-row{left:829px;width:271px;height:46px;border-top:1px solid var(--line);display:flex;align-items:center;font-size:12px;color:#333;padding:0 12px}
.crest{width:20px;height:20px;border-radius:50%;flex:none}
.score-row .team{width:80px;padding-left:10px}
.score-row .time{width:72px}
.score-row .away{width:50px;text-align:right;padding-right:10px}
.chev{left:829px;width:271px}
.review{left:829px;width:271px;display:flex;gap:18px;padding:0 2px}
.review-thumb{width:86px;height:86px;border-radius:50%;flex:none}
.review h4,.euro h4{font-weight:400;font-size:13px;color:#333;line-height:18px}
.review .date,.euro .date{color:var(--red);font-size:12px;margin:6px 0 4px}
.euro .date{color:#333;font-weight:600}
.review p{font-size:11.5px;line-height:17px;color:#444}
.euro{left:829px;width:271px;display:flex;gap:18px}
.euro-thumb{width:86px;height:86px;flex:none}
.divider{left:829px;width:271px;height:1px;background:var(--line)}
.video{left:829px;width:271px;height:161px}
.video-caption{left:829px;width:271px;text-align:center;font-size:15px;color:#333}
.social-box{top:2683px;width:80px;height:82px;color:var(--white);text-align:center;font-size:12px;line-height:15px;padding-top:12px}
.social-box i{display:block;width:20px;height:20px;background:rgba(255,255,255,.9);margin:0 auto 7px}
/* footer */
.site-footer{left:0;top:2909px;width:1200px;height:272px;background:var(--dark);color:#bbb}
.foot-col{top:52px}
.foot-col h5{font-family:"Roboto Condensed",sans-serif;font-weight:700;font-size:16px;color:var(--white);text-transform:uppercase;letter-spacing:.5px;margin-bottom:20px}
.foot-col p{font-size:11.5px;line-height:20px}
.signup{display:flex;margin-top:20px}
.signup span{width:140px;height:38px;background:var(--white);color:#999;font-size:11px;padding:12px 10px}
.signup b{width:76px;height:38px;background:var(--blue);color:var(--white);font-size:12px;font-weight:600;padding:11px 12px}
.foot-list{list-style:none;font-size:13px}
.foot-list li{margin-bottom:18px}
.foot-list li::before{content:"›";margin-right:12px;color:#ccc}
.contact-line{display:flex;align-items:center;gap:14px;font-size:13px;margin-top:12px}
.bottom-bar{left:0;top:3181px;width:1200px;height:56px;background:var(--blue);color:var(--white);font-size:11.5px}
.bottom-bar .copy{left:97px;top:20px}
.bottom-links{right:100px;top:20px;display:flex;gap:10px}
</style>
</head>
<body>

<div class="abs top-bar">
  <div class="abs top-links"><span>Advertise</span><span>Contact Us</span><span>Society</span></div>
  <div class="abs top-call">
    <svg width="13" height="13" viewBox="0 0 24 24"><path fill="#ddd" d="M6.6 10.8a15 15 0 006.6 6.6l2.2-2.2a1 1 0 011-.25 11 11 0 003.6.6 1 1 0 011 1V20a1 1 0 01-1 1A17 17 0 013 4a1 1 0 011-1h3.5a1 1 0 011 1 11 11 0 00.6 3.6 1 1 0 01-.25 1z"/></svg>
    <span>Call Us : +1 555 - 014 - 2290</span>
  </div>
  <div class="abs top-social"><i></i><i></i><i></i><i></i><i></i></div>
  <div class="abs top-search"><svg width="16" height="16" viewBox="0 0 24 24"><circle cx="10" cy="10" r="6.5" fill="none" stroke="#222" stroke-width="2.6"/><path d="M15 15l6 6" stroke="#222" stroke-width="2.8"/></svg></div>
</div>

<header class="abs site-header">
  <div class="abs brand">HARLOW SPORTS <span class="brand-dot"></span></div>
  <nav class="abs main-nav"><span>Football</span><span>Tennis</span><span>Motorsports</span><span>Cycling</span><span>Rugby</span><span>All Sports</span><span>Video</span><span>More</span></nav>
</header>

<section class="abs hero" role="img" aria-label="Stadium under floodlights with two footballers jumping for the ball">
  <div class="abs hero-figure"></div>
  <div class="abs hero-caption">
    <h1>HARLOW SPORTS</h1>
    <p>Lorem ipsum dolor sit amet, consectetur adipiscing elit, sed do eiusmod tempor incididunt ut labore et dolore magna aliqua. Ut enim ad minim veniam, quis nostrud exercitation ullamco laboris nisi ut aliquip ex ea commodo consequat.</p>
    <svg class="abs hero-arrows" width="42" height="28" viewBox="0 0 42 28"><path d="M14 4L5 14l9 10M28 4l9 10-9 10" fill="none" stroke="#fff" stroke-width="3"/></svg>
  </div>
</section>

<h2 class="abs section-title" style="left:97px;top:612px">Featured &amp; Videos</h2>

<article class="abs post-card" style="top:667px">
  <div class="post-image" role="img" aria-label="Two cheering football fans in yellow shirts holding a ball" style="background:linear-gradient(135deg,#4caf50 0%,#d9c24a 45%,#c8a13a 70%,#3c8f3a 100%)"><span class="tag-big">Prime League</span></div>
  <div class="post-head">
    <span class="post-icon"><svg width="16" height="16" viewBox="0 0 20 20"><circle cx="10" cy="10" r="8" fill="none" stroke="#e3202c" stroke-width="2"/><circle cx="10" cy="10" r="3" fill="#e3202c"/></svg></span>
    <div><div class="post-title">Dorvale can show against Germany why he could be Rovers’s Castane</div>
    <div class="post-meta"><span>March 25, 2016</span><span>2 comments</span><span>by Daniel</span></div></div>
  </div>
  <p class="excerpt">Lorem ipsum dolor sit amet, consectetur adipiscing elit, sed do eiusmod tempor incididunt ut labore et dolore magna aliqua. Ut enim ad minim veniam, quis nostrud exercitation ullamco laboris nisi ut aliquip ex ea commodo consequat. Duis aute irure dolor in reprehenderit in voluptate velit esse cillum dolore eu fugiat nulla pariatur....</p>
  <p class="more">Continue reading &gt;&gt;</p>
</article>

<article class="abs post-card" style="top:1148px">
  <div class="post-image" role="img" aria-label="Mountain biker riding over rocky peaks at sunset" style="background:linear-gradient(160deg,#f2b98a 0%,#c0703f 40%,#6b3a2a 75%,#2d1d1a 100%)"><span class="tag-big">Prime League</span></div>
  <div class="post-head">
    <span class="post-icon"><svg width="16" height="16" viewBox="0 0 20 20"><circle cx="10" cy="10" r="8" fill="none" stroke="#e3202c" stroke-width="2"/><circle cx="10" cy="10" r="3" fill="#e3202c"/></svg></span>
    <div><div class="post-title">Dorvale can show against Germany why he could be Rovers’s Castane</div>
    <div class="post-meta"><span>March 25, 2016</span><span>2 comments</span><span>by Daniel</span></div></div>
  </div>
  <p class="excerpt">Lorem ipsum dolor sit amet, consectetur adipiscing elit, sed do eiusmod tempor incididunt ut labore et dolore magna aliqua. Ut enim ad minim veniam, quis nostrud exercitation ullamco laboris nisi ut aliquip ex ea commodo consequat. Duis aute irure dolor in reprehenderit in voluptate velit esse cillum dolore eu fugiat nulla pariatur....</p>
  <p class="more">Continue reading &gt;&gt;</p>
</article>

<h2 class="abs section-title blue" style="left:97px;top:1622px">Sports News</h2>

<div class="abs news-item" style="left:97px;top:1683px">
  <div class="news-image" role="img" aria-label="Football players chasing a ball on grass" style="background:linear-gradient(180deg,#9fbf5a 0%,#6c9a35 60%,#4d7a25 100%)"></div>
  <div class="news-head"><span class="tag-small">Football</span><span class="news-title">Dorvale can show against</span></div>
  <p class="excerpt">Lorem ipsum dolor sit amet, consectetur adipiscing elit, sed do eiusmod tempor incididunt ut labore et dolore magna aliqua. Ut enim ad minim veniam, quis nostrud</p>
  <div class="news-foot"><span class="stars">★★★<b>★★</b></span><span>Sports News</span><span>1 hour ago</span></div>
</div>
<div class="abs news-item" style="left:464px;top:1683px">
  <div class="news-image" role="img" aria-label="Tennis player hitting a ball on a clay court" style="background:linear-gradient(180deg,#2e6b4a 0%,#3f7d56 45%,#c26a45 75%,#b85c3a 100%)"></div>
  <div class="news-head"><span class="tag-small">Tennis</span><span class="news-title">Dorvale can show against</span></div>
  <p class="excerpt">Lorem ipsum dolor sit amet, consectetur adipiscing elit, sed do eiusmod tempor incididunt ut labore et dolore magna aliqua. Ut enim ad minim veniam, quis nostrud</p>
  <div class="news-foot"><span class="stars">★★★<b>★★</b></span><span>Sports News</span><span>1 hour ago</span></div>
</div>
<div class="abs news-item" style="left:97px;top:2031px">
  <div class="news-image" role="img" aria-label="Road cyclist racing along a rail" style="background:linear-gradient(180deg,#e8e8e6 0%,#b8b8b4 50%,#6e6e6a 100%)"></div>
  <div class="news-head"><span class="tag-small">Cycling</span><span class="news-title">Dorvale can show against</span></div>
  <p class="excerpt">Lorem ipsum dolor sit amet, consectetur adipiscing elit, sed do eiusmod tempor incididunt ut labore et dolore magna aliqua. Ut enim ad minim veniam, quis nostrud</p>
  <div class="news-foot"><span class="stars">★★★<b>★★</b></span><span>Sports News</span><span>1 hour ago</span></div>
</div>
<div class="abs news-item" style="left:464px;top:2031px">
  <div class="news-image" role="img" aria-label="Rugby players in a night stadium" style="background:radial-gradient(ellipse at 50% 30%,#5b8bd0 0%,#1e3568 45%,#0a1430 100%)"></div>
  <div class="news-head"><span class="tag-small">Rugby</span><span class="news-title">Dorvale can show against</span></div>
  <p class="excerpt">Lorem ipsum dolor sit amet, consectetur adipiscing elit, sed do eiusmod tempor incididunt ut labore et dolore magna aliqua. Ut enim ad minim veniam, quis nostrud</p>
  <div class="news-foot"><span class="stars">★★★<b>★★</b></span><span>Sports News</span><span>1 hour ago</span></div>
</div>

<article class="abs post-card" style="top:2389px">
  <div class="post-image" role="img" aria-label="Smiling tennis player holding a racket outdoors" style="background:linear-gradient(180deg,#bcd6ea 0%,#e3d6c6 50%,#c7a88c 80%,#8a9a6a 100%)"><span class="tag-big">Prime League</span></div>
  <div class="post-head">
    <span class="post-icon"><svg width="16" height="16" viewBox="0 0 20 20"><circle cx="10" cy="10" r="8" fill="none" stroke="#e3202c" stroke-width="2"/><circle cx="10" cy="10" r="3" fill="#e3202c"/></svg></span>
    <div><div class="post-title">Dorvale can show against Germany why he could be Rovers’s Castane</div>
    <div class="post-meta"><span>March 25, 2016</span><span>2 comments</span><span>by Daniel</span></div></div>
  </div>
  <p class="excerpt">Lorem ipsum dolor sit amet, consectetur adipiscing elit, sed do eiusmod tempor incididunt ut labore et dolore magna aliqua. Ut enim ad minim veniam, quis nostrud exercitation ullamco laboris nisi ut aliquip ex ea commodo consequat. Duis aute irure dolor in reprehenderit in voluptate velit esse cillum dolore eu fugiat nulla pariatur....</p>
  <p class="more">Continue reading &gt;&gt;</p>
</article>

<div class="abs side-head" style="top:667px">All Scores</div>
<div class="abs fixture-title" style="top:730px"><b>Cup of Champions</b>Qualifying Round 1</div>
<div class="abs score-row" style="top:788px"><span class="crest" style="background:#6a4aa0"></span><span class="team">Arvenfield</span><span class="time">17:00FC</span><span class="away">Solano</span><span class="crest" style="background:#c9a56a"></span></div>
<div class="abs score-row" style="top:834px"><span class="crest" style="background:#444"></span><span class="team">B36 Norvik</span><span class="time">17:00FC</span><span class="away">Marenza</span><span class="crest" style="background:#d23a3a"></span></div>
<div class="abs score-row" style="top:880px;border-bottom:1px solid var(--line)"><span class="crest" style="background:#9a9a50"></span><span class="team">Arvenfield</span><span class="time">17:00FC</span><span class="away">Solano</span><span class="crest" style="background:#3a8a5a"></span></div>
<svg class="abs chev" style="top:940px" width="271" height="14" viewBox="0 0 271 14"><path d="M131 2l4.5 4 4.5-4M131 7l4.5 4 4.5-4" fill="none" stroke="#2d8ed3" stroke-width="1.6"/></svg>

<div class="abs side-head" style="top:978px">Recent Reviews</div>
<div class="abs review" style="top:1042px"><div class="review-thumb" role="img" aria-label="Rugby player running with the ball" style="background:radial-gradient(circle,#8a6b55,#3a2e28)"></div><div><h4>Nemo enim ipsam volup</h4><div class="date">July 07, 2016</div><p>Sed ut perspiciatis unde omnis iste natus error sit</p></div></div>
<div class="abs divider" style="top:1152px"></div>
<div class="abs review" style="top:1176px"><div class="review-thumb" role="img" aria-label="Cyclist racing on a road" style="background:radial-gradient(circle,#c8c8c0,#6a6e60)"></div><div><h4>Nemo enim ipsam volup</h4><div class="date">July 07, 2016</div><p>Sed ut perspiciatis unde omnis iste natus error sit</p></div></div>
<div class="abs divider" style="top:1284px"></div>
<div class="abs review" style="top:1306px"><div class="review-thumb" role="img" aria-label="Racing driver in a helmet" style="background:radial-gradient(circle,#c84a4a,#2a2a4a)"></div><div><h4>Nemo enim ipsam volup</h4><div class="date">July 07, 2016</div><p>Sed ut perspiciatis unde omnis iste natus error sit</p></div></div>

<div class="abs side-head" style="top:1433px">Tennis</div>
<div class="abs fixture-title" style="top:1497px"><b>Grasscourt Women</b>Qualifying Round 1</div>
<div class="abs score-row" style="top:1554px"><span class="crest" style="background:#6a4aa0"></span><span class="team">Arvenfield</span><span class="time">17:00FC</span><span class="away">Solano</span><span class="crest" style="background:#c9a56a"></span></div>
<div class="abs score-row" style="top:1600px"><span class="crest" style="background:#444"></span><span class="team">B36 Norvik</span><span class="time">17:00FC</span><span class="away">Marenza</span><span class="crest" style="background:#d23a3a"></span></div>
<div class="abs score-row" style="top:1646px;border-bottom:1px solid var(--line)"><span class="crest" style="background:#9a9a50"></span><span class="team">Arvenfield</span><span class="time">17:00FC</span><span class="away">Solano</span><span class="crest" style="background:#3a8a5a"></span></div>
<svg class="abs chev" style="top:1706px" width="271" height="14" viewBox="0 0 271 14"><path d="M131 2l4.5 4 4.5-4M131 7l4.5 4 4.5-4" fill="none" stroke="#2d8ed3" stroke-width="1.6"/></svg>

<div class="abs side-head" style="top:1750px">Continental 2016</div>
<div class="abs euro" style="top:1823px"><div class="euro-thumb" role="img" aria-label="Ice hockey player in yellow" style="background:linear-gradient(135deg,#e9eef3,#d8b43a 60%,#3a5a8a)"></div><div><h4>Sed ut perspiciatis unde omnis iste natus error</h4><div class="date">July 07, 2016</div></div></div>
<div class="abs divider" style="top:1930px"></div>
<div class="abs euro" style="top:1953px"><div class="euro-thumb" role="img" aria-label="Sprinter at the starting line" style="background:linear-gradient(135deg,#d8d0c8,#8a3a2a 60%,#3a2a26)"></div><div><h4>Sed ut perspiciatis unde omnis iste natus error</h4><div class="date">July 07, 2016</div></div></div>
<div class="abs divider" style="top:2058px"></div>
<div class="abs euro" style="top:2078px"><div class="euro-thumb" role="img" aria-label="Skier carving through snow" style="background:linear-gradient(135deg,#f2f4f8,#c84a5a 55%,#e8eaf0)"></div><div><h4>Sed ut perspiciatis unde omnis iste natus error</h4><div class="date">July 07, 2016</div></div></div>

<div class="abs side-head" style="top:2199px">Videos</div>
<div class="abs video" style="top:2257px" role="img" aria-label="Video still of footballers in a stadium"><svg width="271" height="161" viewBox="0 0 271 161"><defs><linearGradient id="v1" x1="0" y1="0" x2="0" y2="1"><stop offset="0" stop-color="#8aa0b0"/><stop offset=".55" stop-color="#5a6a58"/><stop offset="1" stop-color="#3e6a30"/></linearGradient></defs><rect width="271" height="161" fill="url(#v1)"/><circle cx="135" cy="88" r="24" fill="rgba(255,255,255,.35)" stroke="#fff" stroke-width="2"/><path d="M128 77l16 11-16 11z" fill="#fff"/></svg></div>
<div class="abs video-caption" style="top:2430px">Nemo enim ipsam voluptatem</div>
<div class="abs video" role="img" aria-label="Footballers in yellow contesting the ball" style="top:2471px;background:linear-gradient(180deg,#2a3a2a 0%,#4a6a3a 50%,#3a7a2a 100%)"></div>
<div class="abs video-caption" style="top:2646px">Nemo enim ipsam voluptatem</div>

<div class="abs social-box" style="left:829px;background:#3b5b9a"><i></i>68,876<br>Fans</div>
<div class="abs social-box" style="left:925px;background:#2aa6e0"><i></i>65<br>Followers</div>
<div class="abs social-box" style="left:1020px;background:#d23b2e"><i></i>8,961<br>Followers</div>

<footer class="abs site-footer">
  <div class="abs foot-col" style="left:97px;width:200px">
    <h5>About Our Company</h5>
    <p>At vero eos et accusamus et iusto odio dignissimos ducimus qui blanditiis praesentium voluptatum deleniti atque corrupti quos dolores et quas mol eos et accusamus et iusto odio dignissimos</p>
  </div>
  <div class="abs foot-col" style="left:367px;width:240px">
    <h5>Newsletter</h5>
    <p>Excepteur sint occaecat cupidatat non proident, sunt in culpa qui</p>
    <div class="signup"><span>Enter your email...</span><b>SIGN UP</b></div>
  </div>
  <div class="abs foot-col" style="left:658px;width:220px">
    <h5>Recent Posts</h5>
    <ul class="foot-list"><li>Post Format: Standard</li><li>Post Format: Gallery</li><li>Post Format: Quote</li><li>Post Format: Audio (Self Hosted)</li></ul>
  </div>
  <div class="abs foot-col" style="left:928px;width:200px">
    <h5>Contact Info</h5>
    <p>Harlow Sports<br>PO BOX 12, Westmere</p>
    <div class="contact-line"><svg width="16" height="16" viewBox="0 0 24 24"><path fill="#bbb" d="M6.6 10.8a15 15 0 006.6 6.6l2.2-2.2a1 1 0 011-.25 11 11 0 003.6.6 1 1 0 011 1V20a1 1 0 01-1 1A17 17 0 013 4a1 1 0 011-1h3.5a1 1 0 011 1 11 11 0 00.6 3.6 1 1 0 01-.25 1z"/></svg><span style="font-size:15px">+1 555 0187 3321</span></div>
    <div class="contact-line"><svg width="16" height="12" viewBox="0 0 16 12"><rect x="1" y="1" width="14" height="10" fill="none" stroke="#bbb" stroke-width="1.5"/><path d="M1 1l7 6 7-6" fill="none" stroke="#bbb" stroke-width="1.5"/></svg><span>info@harlowsports.com</span></div>
  </div>
</footer>

<div class="abs bottom-bar">
  <div class="abs copy">Copyright @ 2016, Harlow Sports. All Rights Reserved.</div>
  <div class="abs bottom-links"><span>HOME</span>|<span>ABOUT US</span>|<span>DISCLAIMER</span>|<span>CONTACT US</span></div>
</div>

</body>
</html>
```